Fitness Equipment Repair Business Needs a Catchy New Business Card

We have an existing business card, however, it is quite plain and boring. We are expanding primarily in the commercial area (gyms, studios, apartment complexes etc). The business card will serve as eye candy to those managers/owners that can't be met for a face to face.
Originally I was planning for a brochure as well, but all of our information is better summarized on our website. (brasswheelservicing.ca).
I would like the card to match the colour scheme of the website and utilize the logo. It should have a professional clean feel to it, however, a little colouring outside the lines wouldn't hurt.
The example card is for my service technician (Corwin Haldane). If possible I would like to be able to edit the text to use for more than one person.

Industry/Entity Type

Appliance Repair

Contact Information for Business Card

Clean, crisp and professional but needs to be eye catching. Preferably using the black, white and red colour scheme matching the website. Double sided would be nice, but is not necessary.

Colors
ec1f27
ffffff
000000

Requirements
Must have
• Must be able to edit name, phone number and title to use for multiple people. Must show the company website (brasswheelservicing.ca).

```html
<!DOCTYPE html>
<html lang="en">
<head>
<meta charset="utf-8">
<title>Brass Wheel Servicing – Business Card</title>
<link href="https://fonts.googleapis.com/css2?family=Cinzel:wght@400;600&family=Open+Sans:wght@400;600&display=swap" rel="stylesheet">
<style>
  :root {
    --red: #ec1f27;
    --white: #ffffff;
    --black: #000000;
    --stage: #e9e6e3;
    --display: "Cinzel", serif;
    --body: "Open Sans", sans-serif;
  }
  html, body { margin: 0; padding: 0; }
  body {
    width: 1200px; height: 900px; overflow: hidden;
    background: var(--stage); position: relative;
    font-family: var(--body);
  }
  .card { position: absolute; overflow: hidden; box-shadow: 0 6px 18px rgba(0,0,0,.25); }

  /* Front */
  .card--front { left: 77px; top: 34px; width: 590px; height: 363px; background: var(--white); }
  .front-bands { position: absolute; left: 0; top: 0; }
  .brand { position: absolute; display: flex; align-items: center; }
  .brand-mark { background: var(--red); flex: none; }
  .brand-name { font-family: var(--display); font-weight: 400; white-space: nowrap; letter-spacing: .5px; }
  .card--front .brand { left: 56px; top: 76px; }
  .card--front .brand-mark { width: 44px; height: 44px; margin-right: 53px; }
  .card--front .brand-name { font-size: 30px; color: var(--black); }

  .person { position: absolute; right: 316px; top: 258px; text-align: right; color: var(--white); }
  .person-name { font-size: 20px; font-weight: 600; line-height: 1.2; }
  .person-title { font-size: 15px; line-height: 1.3; }

  .contacts { position: absolute; left: 294px; top: 250px; list-style: none; margin: 0; padding: 0; color: var(--white); font-size: 15px; }
  .contacts li { display: flex; align-items: center; height: 21px; }
  .contacts svg { width: 12px; height: 12px; margin-right: 13px; fill: var(--white); }
  .address { position: absolute; left: 0; right: 0; top: 322px; text-align: center; color: var(--white); font-size: 15px; }

  /* Back */
  .card--back { left: 388px; top: 505px; width: 567px; height: 352px; background: var(--black); }
  .card--back .brand { left: 52px; top: 138px; }
  .card--back .brand-mark { width: 40px; height: 40px; margin-right: 57px; }
  .card--back .brand-name { font-size: 28px; color: var(--white); }
  .website { position: absolute; left: 190px; top: 205px; color: var(--red); font-size: 14px; font-weight: 600; }
  .tagline { position: absolute; left: 0; right: 0; top: 265px; text-align: center; color: var(--white);
    font-family: var(--display); font-size: 21px; line-height: 1.25; margin: 0; font-weight: 400; }
</style>
</head>
<body>

<section class="card card--front" aria-label="Business card front">
  <svg class="front-bands" width="590" height="363" viewBox="0 0 590 363" aria-hidden="true">
    <polygon points="0,191 414,191 385,225 0,225" fill="#ec1f27"/>
    <polygon points="414,191 590,191 590,363 0,363 0,225 385,225" fill="#000"/>
    <line x1="0" y1="226" x2="386" y2="226" stroke="#fff" stroke-width="2"/>
  </svg>
  <div class="brand">
    <span class="brand-mark"></span>
    <span class="brand-name">Brass Wheel Servicing</span>
  </div>
  <div class="person">
    <div class="person-name">Corwin Haldane</div>
    <div class="person-title">Managing Director</div>
  </div>
  <ul class="contacts">
    <li><svg viewBox="0 0 24 24"><path d="M6.6 10.8a15 15 0 0 0 6.6 6.6l2.2-2.2c.3-.3.7-.4 1-.2 1.1.4 2.3.6 3.6.6.6 0 1 .4 1 1V20c0 .6-.4 1-1 1A17 17 0 0 1 3 4c0-.6.4-1 1-1h3.5c.6 0 1 .4 1 1 0 1.3.2 2.5.6 3.6.1.3 0 .7-.2 1z"/></svg>044-555 010 230</li>
    <li><svg viewBox="0 0 24 24"><path d="M7 1h10a2 2 0 0 1 2 2v18a2 2 0 0 1-2 2H7a2 2 0 0 1-2-2V3a2 2 0 0 1 2-2zm0 3v14h10V4z"/></svg>044-555 010 230</li>
    <li><svg viewBox="0 0 24 24"><path d="M2 5h20v14H2zm2 2v.5l8 5 8-5V7l-8 5z"/></svg>info@brasswheelservicing.ca</li>
  </ul>
  <div class="address">12345, Address Goes Here Country Name, 123456.</div>
</section>

<section class="card card--back" aria-label="Business card back">
  <div class="brand">
    <span class="brand-mark"></span>
    <span class="brand-name">Brass Wheel Servicing</span>
  </div>
  <div class="website">www.brasswheelservicing.ca</div>
  <p class="tagline">When your equipment can't finish<br>their workout, give us a call!</p>
</section>

</body>
</html>
```